Brimvale Crest Homes needs a business card

We need a business card for a new company in Canada, Ontario. Our company is all about luxury contraction homes for our clients. Our product and services are custom projects design. Under the business logo that will be created, we want a slogan that will be a memorable phrase for consumers to remember us to tell their friends and relatives.

Additional infomation
- Teodoro Vanlesky
- President / Ceo
-519.304.7718

Find point what luxury construction products and services can be done

We like to see colors:
- #663300
- and something other colors or color that would attract the client needs and wants

The final design should communicate leads from new or old clients that will grow our empire. Most of all, we try to work among the budget that clients want

NOTE
- we also need an icon for the business (Example: Instagram, Facebook, and Whatsapp icons)
- We want the company name to be remembered easily for clients and our distributors who would get our orders.
- we need an icon on the business cards: Facebook and Instagram.

Thanks,
Brimvale Crest Homes

```html
<!DOCTYPE html>
<html lang="en">
<head>
<meta charset="utf-8">
<title>Brimvale Crest Homes – Business Card</title>
<link rel="stylesheet" href="https://fonts.googleapis.com/css2?family=Roboto:wght@400;500;700&display=swap">
<style>
  :root {
    --brown: #663300;
    --brown-light: #8a4716;
    --brown-dark: #4f2600;
    --paper: #f7f7f5;
    --rule-grey: #b9b9b9;
    --backdrop: #e9e4dd;
    --ink-light: #ffffff;
  }
  * { box-sizing: border-box; margin: 0; padding: 0; }
  html, body { width: 1200px; height: 780px; overflow: hidden; }
  body {
    background: var(--backdrop);
    font-family: "Roboto", Arial, sans-serif;
    position: relative;
  }
  .card {
    position: absolute;
    top: 236px;
    width: 540px;
    height: 309px;
    border-radius: 3px;
    overflow: hidden;
    box-shadow: 0 6px 18px rgba(60, 35, 10, 0.25);
  }
  .card--front { left: 45px; background: var(--paper); }
  .card--back {
    left: 615px;
    background: radial-gradient(ellipse at 30% 60%, var(--brown-light), var(--brown) 55%, var(--brown-dark));
  }

  /* Company name, set in the card's text face */
  .company-name {
    font-family: "Roboto", Arial, sans-serif;
    font-weight: 700;
    color: var(--brown);
    font-size: 38px;
    letter-spacing: 0.2px;
    line-height: 1;
  }
  .tagline {
    margin-top: 10px;
    color: var(--brown);
    font-size: 14.5px;
    font-weight: 500;
    letter-spacing: 0.3px;
    white-space: nowrap;
  }

  /* Front */
  .front__brand {
    position: absolute; left: 0; top: 0; width: 100%; height: 178px;
    display: flex; flex-direction: column; align-items: center; justify-content: center;
    padding-top: 10px;
  }
  .front__rule {
    position: absolute; left: 0; top: 178px; width: 100%; height: 9px;
    background: var(--rule-grey);
  }
  .front__details {
    position: absolute; left: 0; top: 187px; width: 100%; height: 122px;
    background: radial-gradient(ellipse at 40% 40%, var(--brown-light), var(--brown) 70%);
    display: flex; align-items: center; color: var(--ink-light);
  }
  .person { width: 270px; text-align: right; padding-right: 22px; }
  .person__name { font-size: 21px; font-weight: 500; }
  .person__role { font-size: 14px; margin-top: 4px; }
  .divider { width: 1.5px; height: 62px; background: rgba(255,255,255,0.8); }
  .contacts { list-style: none; padding-left: 20px; font-size: 13px; line-height: 22px; }
  .contacts li { display: flex; align-items: center; gap: 8px; }
  .contacts svg { width: 12px; height: 12px; flex: none; }

  /* Back */
  .back__band {
    position: absolute; left: 0; top: 82px; width: 100%; height: 132px;
    background: var(--paper);
    display: flex; flex-direction: column; align-items: center; justify-content: center;
  }
  .back__line {
    position: absolute; left: 0; width: 100%; height: 3px; background: var(--paper);
  }
  .back__line--top { top: 72px; }
  .back__line--bottom { top: 222px; }
  .socials {
    position: absolute; left: 40px; top: 244px; display: flex; gap: 10px;
  }
  .socials span {
    width: 22px; height: 22px; border-radius: 4px; background: var(--paper); display: block;
  }
</style>
</head>
<body>

  <section class="card card--front" aria-label="Business card front">
    <div class="front__brand">
      <h1 class="company-name">Brimvale Crest Homes</h1>
      <p class="tagline">- HOME RENOVATIONS - CUSTOM PROJECT DESIGN -</p>
    </div>
    <div class="front__rule"></div>
    <div class="front__details">
      <div class="person">
        <p class="person__name">Teodoro Vanlesky</p>
        <p class="person__role">President / Ceo</p>
      </div>
      <div class="divider"></div>
      <ul class="contacts">
        <li>
          <svg viewBox="0 0 12 12"><rect x="1.5" y="1.5" width="9" height="9" fill="none" stroke="#fff" stroke-width="1.3"/></svg>
          519.304.7718
        </li>
        <li>
          <svg viewBox="0 0 12 12"><rect x="1" y="2.5" width="10" height="7" fill="none" stroke="#fff" stroke-width="1.2"/><path d="M1 2.5 L6 6.5 L11 2.5" fill="none" stroke="#fff" stroke-width="1.2"/></svg>
          info@brimvalecrest.ca
        </li>
        <li>
          <svg viewBox="0 0 12 12"><circle cx="6" cy="6" r="5" fill="none" stroke="#fff" stroke-width="1.2"/><ellipse cx="6" cy="6" rx="2.2" ry="5" fill="none" stroke="#fff" stroke-width="1"/><path d="M1 6 H11" stroke="#fff" stroke-width="1"/></svg>
          www.brimvalecrest.ca
        </li>
      </ul>
    </div>
  </section>

  <section class="card card--back" aria-label="Business card back">
    <div class="back__line back__line--top"></div>
    <div class="back__band">
      <h2 class="company-name">Brimvale Crest Homes</h2>
      <p class="tagline">- HOME RENOVATIONS - CUSTOM PROJECT DESIGN -</p>
    </div>
    <div class="back__line back__line--bottom"></div>
    <div class="socials" aria-label="Social media">
      <span></span>
      <span></span>
    </div>
  </section>

</body>
</html>
```